Web form face-lift for an online startup

We are a web startup building a SaaS application for the freight industry. The project is mainly dedicated to the paint the main form that our customer are using along the search results that the they get. All details are in the attached documents.
Updates
The application serves the Freight Forwarders community so please think towards this industry when using background images, banners, colors, icons, etc. Computer and technology images are irrelevant.
Customer fields at the top of the page is actually part of the form.
Target Market(s)
Usually business users (Sales people, procurement, shippers, freight forwarders). Some are less tech savvy and some appreciate the new trendy web apps.
Industry/Entity Type
Building
Colors
Designer to choose colors to be used in the design.
Look and feel
Each slider illustrates characteristics of the customer's brand and the style your logo design should communicate.

```html
<!DOCTYPE html>
<html lang="en">
<head>
<meta charset="utf-8">
<title>FreightNest</title>
<link rel="stylesheet" href="https://fonts.googleapis.com/css2?family=Open+Sans:wght@300;400;600;700&family=Montserrat:wght@400;700&display=swap">
<style>
:root{
  --red:#d8262f;
  --red-dark:#b51a22;
  --ink:#2b2b2b;
  --grey-text:#777;
  --light:#f2f2f2;
  --footer:#383838;
  --footer-line:#555;
  --white:#fff;
  --panel:rgba(20,20,20,.78);
}
*{box-sizing:border-box;margin:0;padding:0}
html,body{width:1200px;height:2553px;overflow:hidden;background:#fff}
body{font-family:"Open Sans",Arial,sans-serif;color:var(--ink);position:relative}
.abs{position:absolute}

/* header */
.site-header{position:absolute;left:0;top:0;width:1200px;height:96px;background:#f7f7f7;border-bottom:4px solid var(--red)}
.brand-name{position:absolute;left:117px;top:24px;font-size:33px;font-weight:600;line-height:44px;color:#111;white-space:nowrap}
.main-nav{position:absolute;left:451px;top:0;display:flex;z-index:4}
.main-nav a{display:block;height:92px;line-height:100px;padding:0 20px;font-size:16px;color:#333;text-decoration:none}
.main-nav a.active{background:var(--red);color:#fff;height:92px;border-radius:0 0 3px 3px;padding:0 18px;margin-right:6px}

/* hero */
.hero{position:absolute;left:0;top:96px;width:1200px;height:617px;overflow:hidden}
.hero-photo{position:absolute;inset:0;background:linear-gradient(180deg,#6f7c8f 0%,#a9b2bf 35%,#8e9aa6 55%,#3d6f9b 72%,#35485a 100%)}
.hero-arrow{position:absolute;top:282px;width:57px;height:57px;background:rgba(20,20,20,.8);display:flex;align-items:center;justify-content:center}
.hero-caption{position:absolute;left:643px;top:198px;width:457px;height:163px;background:var(--panel);color:#fff;text-align:right;padding:12px 10px 0 0}
.hero-caption .title{font-size:33px;font-weight:400;line-height:46px;text-align:left;padding-left:10px;white-space:nowrap}
.hero-caption .line{font-size:29px;line-height:42px;text-transform:uppercase;border-right:5px solid var(--red);padding-right:10px;display:inline-block;margin-top:2px;white-space:nowrap}
.quote-bar{position:absolute;left:88px;top:510px;width:1012px;height:107px;background:var(--panel)}
.quote-tag{position:absolute;left:100px;top:487px;width:294px;height:49px;background:var(--red);color:#fff;font-size:23px;line-height:49px;padding-left:8px;clip-path:polygon(0 0,100% 0,93% 100%,0 100%)}
.quote-type{position:absolute;top:520px;display:flex;align-items:center;color:#fff;font-size:17px}
.quote-type i{display:inline-block;width:23px;height:23px;background:#fff;margin-right:14px}
.quote-field{position:absolute;top:566px;height:36px;background:#fff;font-size:13px;color:#888;line-height:36px;padding-left:8px;border:1px solid #ccc}
.quote-field .req{position:absolute;right:6px;top:0;color:var(--red);font-size:16px}
.quote-field .caret{position:absolute;right:8px;top:15px;border:5px solid transparent;border-top-color:#333}
.quote-submit{position:absolute;left:896px;top:566px;width:160px;height:36px;background:var(--red);color:#fff;font-size:19px;text-align:center;line-height:36px}

/* welcome */
.welcome{position:absolute;left:0;top:713px;width:1200px;height:113px;border-top:4px solid var(--red);background:#fff}
.welcome h1{position:absolute;left:100px;top:12px;font-size:41px;font-weight:400;color:#111;white-space:nowrap}
.welcome h1 b{font-weight:600}
.welcome p{position:absolute;left:100px;top:68px;font-size:17px;color:#222}
.welcome-panel{position:absolute;left:776px;top:-4px;width:424px;height:113px;background:var(--red);clip-path:polygon(18% 0,100% 0,100% 100%,0 100%)}
.search{position:absolute;left:857px;top:20px;width:246px;height:36px;background:#fff;border:3px solid #f4c6c8;font-size:13px;color:#777;line-height:30px;padding-left:12px}
.search-btn{position:absolute;right:-1px;top:-1px;width:32px;height:32px;background:var(--red);display:flex;align-items:center;justify-content:center}
.social-row{position:absolute;left:858px;top:72px;display:flex;gap:20px}
.social-row i{display:block;width:24px;height:24px;border-radius:50%;background:#fff}

/* category strip */
.categories{position:absolute;left:0;top:826px;width:1200px;height:164px;background:var(--light);border-bottom:1px solid #e0e0e0}
.cat{position:absolute;top:36px;width:130px;text-align:center;font-size:13px;color:#333}
.cat .ring{width:64px;height:64px;margin:0 auto 24px;border-radius:50%;background:#fff;border:1px solid #d6d6d6;display:flex;align-items:center;justify-content:center}
.cat-divider{position:absolute;top:28px;width:1px;height:110px;background:#dcdcdc}

/* services */
.services{position:absolute;left:0;top:990px;width:1200px;height:765px;background:#fff}
.services-map{position:absolute;left:60px;top:90px;width:1060px;height:560px;background:radial-gradient(ellipse at center,#f0f0f0 0%,#f7f7f7 55%,#fff 80%)}
.services h2{position:absolute;left:0;width:1200px;top:52px;text-align:center;font-family:"Montserrat",Arial,sans-serif;font-size:40px;font-weight:700;color:var(--red);letter-spacing:1px}
.services .sub{position:absolute;left:0;width:1200px;top:112px;text-align:center;font-size:14px;color:#777}
.services .rule{position:absolute;left:548px;top:104px;width:104px;height:2px;background:#aaa}
.service{position:absolute;width:290px}
.service h3{font-size:18px;font-weight:600;color:#222;margin-bottom:6px}
.service h3.hl{color:var(--red)}
.service p{font-size:13px;line-height:18px;color:#888}
.service p b{color:var(--red);font-weight:600}
.service-icon{position:absolute;width:110px;height:110px;display:flex;align-items:center;justify-content:center}
.counter-label{position:absolute;left:330px;top:670px;width:200px;text-align:right;font-size:14px;line-height:18px;color:#333}
.counter-label em{font-style:normal;color:var(--red)}
.counter{position:absolute;left:556px;top:672px;display:flex;gap:4px}
.counter span{width:24px;height:30px;border:1px solid #bbb;box-shadow:0 1px 2px #ccc;font-size:16px;text-align:center;line-height:28px;color:#333}
.create-ad{position:absolute;left:698px;top:672px;width:158px;height:34px;background:var(--red);color:#fff;font-size:19px;text-align:center;line-height:34px}

/* testimonials */
.testimonials{position:absolute;left:0;top:1755px;width:1200px;height:345px;overflow:hidden}
.testimonials-photo{position:absolute;inset:0;background:linear-gradient(110deg,#59667a 0%,#7f8da0 40%,#98a4b4 60%,#5b6a7e 100%)}
.testimonials h2{position:absolute;left:0;width:1200px;top:18px;text-align:center;font-size:40px;font-weight:300;color:#fff}
.testimonials .rule{position:absolute;left:300px;top:86px;width:600px;height:2px;background:var(--red)}
.testimonials blockquote{position:absolute;left:290px;top:118px;width:620px;text-align:center;font-size:15.5px;line-height:26px;color:#fff}
.avatar{position:absolute;left:555px;top:192px;width:94px;height:94px;border-radius:50%;background:#d9d9d9;border:4px solid #fff}
.testimonials .name{position:absolute;left:0;width:1200px;top:300px;text-align:center;font-size:15px;color:#fff}
.t-arrow{position:absolute;top:168px}

/* newsletter */
.newsletter{position:absolute;left:0;top:2100px;width:1200px;height:75px;background:var(--red);color:#fff}
.newsletter .label{position:absolute;left:208px;top:17px;font-size:15px;line-height:19px;font-weight:600}
.nl-input{position:absolute;top:17px;height:39px;background:#fff;font-size:12px;color:#666;line-height:39px;padding-left:18px}
.nl-btn{position:absolute;left:932px;top:17px;width:126px;height:39px;background:#444;font-size:14px;font-weight:700;text-align:center;line-height:39px;color:#fff}

/* footer */
.site-footer{position:absolute;left:0;top:2175px;width:1200px;height:321px;background:var(--footer);color:#fff}
.site-footer h4{position:absolute;font-size:18px;font-weight:400;text-transform:uppercase}
.f-social{position:absolute;left:111px;top:63px;display:flex;gap:14px}
.f-social i{display:block;width:36px;height:36px;border-radius:50%;background:#666}
.f-social i.on{background:var(--red)}
.blog{position:absolute;left:111px;top:178px;width:260px}
.blog .t{font-size:13px}
.blog .d{font-size:10px;color:#e0a040}
.blog p{font-size:12px;line-height:17px;margin-top:2px;color:#ddd}
.blog a{display:block;margin-top:8px;font-family:Georgia,serif;font-size:12px;color:#e0a040;text-decoration:none}
.ad-list{position:absolute;left:447px;top:66px;width:276px;list-style:none}
.ad-list li{height:25.5px;border-bottom:1px solid #8a8a8a;font-size:11px;line-height:22px;padding-left:10px;color:#eee}
.f-field{position:absolute;left:819px;width:277px;background:#eee3e3;font-family:Georgia,serif;font-size:12px;color:#888;padding:4px 8px}
.f-submit{position:absolute;left:1026px;top:264px;width:70px;height:27px;background:var(--red);font-size:12px;text-align:center;line-height:27px;font-weight:600}
.bottom-bar{position:absolute;left:0;top:2496px;width:1200px;height:57px;background:var(--red);color:#fff;font-size:11px}
.bottom-bar span{position:absolute;left:111px;top:26px}
</style>
</head>
<body>

<header class="site-header">
  <div class="brand-name">FreightNest</div>
  <nav class="main-nav">
    <a class="active" href="#">Home</a>
    <a href="#">About Us</a>
    <a href="#">Services</a>
    <a href="#">Divisions</a>
    <a href="#">Locations</a>
    <a href="#">News</a>
    <a href="#">Contact us</a>
  </nav>
</header>

<section class="hero">
  <div class="hero-photo" role="img" aria-label="Large container ship loaded with stacked containers under a cloudy sky"></div>
  <div class="hero-arrow" style="left:0"><svg width="16" height="22"><path d="M12 2 3 11l9 9" stroke="#fff" stroke-width="3" fill="none"/></svg></div>
  <div class="hero-arrow" style="right:0"><svg width="16" height="22"><path d="M4 2l9 9-9 9" stroke="#fff" stroke-width="3" fill="none"/></svg></div>
  <div class="hero-caption">
    <div class="title">Harborline Express Shipping</div>
    <div class="line">ISO Tanks</div><br>
    <div class="line">Container Storage</div>
  </div>
  <div class="quote-bar"></div>
  <div class="quote-tag">GET A FREE QUOTE NOW</div>
  <div class="quote-type" style="left:394px"><i></i>Corporate</div>
  <div class="quote-type" style="left:520px"><i></i>Commercial</div>
  <div class="quote-field" style="left:104px;width:190px">Name<span class="req">*</span></div>
  <div class="quote-field" style="left:309px;width:188px">Phone #<span class="req">*</span></div>
  <div class="quote-field" style="left:511px;width:108px">Move From<span class="caret"></span></div>
  <div class="quote-field" style="left:634px;width:108px">Move To<span class="caret"></span></div>
  <div class="quote-field" style="left:755px;width:106px">Date
    <svg style="position:absolute;right:6px;top:7px" width="22" height="22"><rect x="2" y="4" width="18" height="16" fill="none" stroke="#444" stroke-width="2"/><path d="M2 9h18M7 2v5M15 2v5" stroke="#444" stroke-width="2"/></svg></div>
  <div class="quote-submit">SUBMIT</div>
</section>

<section class="welcome">
  <h1>Welcome To <b>FreightNest Portal</b></h1>
  <p>Lorem Ipsum is simply dummy text of the printing and typesetting industry.</p>
  <div class="welcome-panel"></div>
  <div class="search">Search...
    <div class="search-btn"><svg width="18" height="18"><circle cx="7" cy="7" r="5" stroke="#fff" stroke-width="2.5" fill="none"/><path d="M11 11l5 5" stroke="#fff" stroke-width="3"/></svg></div>
  </div>
  <div class="social-row"><i></i><i></i><i></i><i></i><i></i><i></i></div>
</section>

<section class="categories">
  <div class="cat" style="left:128px"><div class="ring"><svg width="34" height="30"><path d="M2 4h6l4 16h16l4-12H10" fill="none" stroke="#d8262f" stroke-width="3"/><circle cx="14" cy="26" r="2.5" fill="#d8262f"/><circle cx="26" cy="26" r="2.5" fill="#d8262f"/></svg></div>Shipping</div>
  <div class="cat-divider" style="left:258px"></div>
  <div class="cat" style="left:258px"><div class="ring"><svg width="32" height="26"><rect x="2" y="4" width="28" height="20" fill="#d8262f"/></svg></div>Terminals</div>
  <div class="cat-divider" style="left:388px"></div>
  <div class="cat" style="left:388px"><div class="ring"><svg width="36" height="36"><circle cx="18" cy="18" r="15" fill="none" stroke="#d8262f" stroke-width="3"/><rect x="11" y="13" width="14" height="10" fill="#d8262f"/></svg></div>Relocations</div>
  <div class="cat-divider" style="left:518px"></div>
  <div class="cat" style="left:518px"><div class="ring"><svg width="36" height="36"><circle cx="18" cy="18" r="14" fill="#d8262f"/><circle cx="18" cy="18" r="5" fill="#fff"/></svg></div>IT Software</div>
  <div class="cat-divider" style="left:648px"></div>
  <div class="cat" style="left:648px"><div class="ring"><svg width="38" height="30"><rect x="2" y="6" width="22" height="16" fill="#d8262f"/><path d="M24 11h7l5 6v5H24z" fill="#d8262f"/><circle cx="10" cy="25" r="3.5" fill="#444"/><circle cx="30" cy="25" r="3.5" fill="#444"/></svg></div>Logistics</div>
  <div class="cat-divider" style="left:778px"></div>
  <div class="cat" style="left:778px"><div class="ring"><svg width="40" height="30"><path d="M2 16h36l-5 10H7z" fill="#d8262f"/><rect x="10" y="6" width="8" height="10" fill="#d8262f"/><rect x="20" y="9" width="8" height="7" fill="#d8262f"/></svg></div>Freight Services</div>
  <div class="cat-divider" style="left:908px"></div>
  <div class="cat" style="left:908px"><div class="ring"><svg width="40" height="30"><rect x="6" y="5" width="28" height="15" rx="7" fill="#d8262f"/><rect x="4" y="20" width="32" height="3" fill="#444"/><circle cx="11" cy="26" r="3" fill="#444"/><circle cx="29" cy="26" r="3" fill="#444"/></svg></div>ISO Tanks</div>
</section>

<section class="services">
  <div class="services-map" role="img" aria-label="Faint dotted world map behind the service list"></div>
  <h2>SERVICES</h2>
  <div class="rule"></div>
  <div class="sub">Top reasons why to use FreightNest</div>

  <div class="service-icon" style="left:247px;top:178px;border:4px solid var(--red);border-radius:50%;background:#fff"><div role="img" aria-label="Customer support agent illustration" style="width:70px;height:70px;border-radius:50%;background:#e9c9c9"></div></div>
  <div class="service" style="left:400px;top:192px"><h3 class="hl">Looking for clients?</h3><p>Consumer credit from Swift<br>Credit – the best solution for you<br>if you are planning to shop for<br>home and office repairs, a<br>family holiday.</p></div>

  <div class="service-icon" style="left:668px;top:190px"><div role="img" aria-label="Globe with location pin" style="width:90px;height:90px;border-radius:50%;background:linear-gradient(135deg,#e6d6d0,#5b4a48)"></div></div>
  <div class="service" style="left:795px;top:198px"><h3>Visible results</h3><p>In the "Map" section you can<br>see the current locations of<br>your company's and partner<br>companies' cargoes and<br>transport.</p></div>

  <div class="service-icon" style="left:247px;top:350px"><svg width="76" height="76"><rect x="3" y="3" width="70" height="70" rx="6" fill="#d8262f"/><rect x="16" y="30" width="10" height="32" fill="#fff"/><rect x="33" y="20" width="10" height="42" fill="#fff"/><rect x="50" y="36" width="10" height="26" fill="#fff"/></svg></div>
  <div class="service" style="left:400px;top:364px"><h3>Reach target audience</h3><p>Consumer credit from Swift<br>Credit – the best solution for you<br>if you are planning to shop for<br>home and office repairs, a<br>family holiday.</p></div>

  <div class="service-icon" style="left:668px;top:346px"><svg width="96" height="96"><circle cx="48" cy="48" r="40" fill="#d8262f"/><circle cx="48" cy="48" r="18" fill="#fff"/><path d="M40 8h16v22H40zM40 66h16v22H40zM8 40h22v16H8zM66 40h22v16H66z" fill="#fff"/></svg></div>
  <div class="service" style="left:795px;top:356px"><h3>24/7 Online support</h3><p>If you have any inconveniences,<br>feel free to call or e-mail us and<br>you will get an answer each<br>weekday from 9 am to 6 pm.</p></div>

  <div class="service-icon" style="left:247px;top:520px"><svg width="90" height="90"><circle cx="36" cy="36" r="24" fill="#e5e5e5" stroke="#333" stroke-width="8"/><path d="M55 55l24 24" stroke="#d8262f" stroke-width="12" stroke-linecap="round"/></svg></div>
  <div class="service" style="left:400px;top:522px"><h3>Easy and quick</h3><p>After offering a transport or a<br>cargo in FreightNest it will be<br>immediately visible to all your<br>potential clients. It is even easier<br>than calling them.</p></div>

  <div class="service-icon" style="left:668px;top:520px"><svg width="82" height="82"><rect x="4" y="6" width="74" height="66" rx="8" fill="#d8262f"/><rect x="16" y="18" width="50" height="26" fill="#333"/><circle cx="22" cy="58" r="5" fill="#333"/><circle cx="60" cy="58" r="5" fill="#333"/></svg></div>
  <div class="service" style="left:795px;top:522px"><h3>Still unconvinced?</h3><p>Offering cargoes and transport<br>in Portvia will increase the<br>number of your potential clients.<br>Just <b>add your ad right now!</b></p></div>

  <div class="counter-label">Our customers <em>love us.</em><br>So far added ads</div>
  <div class="counter"><span>7</span><span>5</span><span>3</span><span>0</span></div>
  <div class="create-ad">Create Ad</div>
</section>

<section class="testimonials">
  <div class="testimonials-photo" role="img" aria-label="Close-up of coins, a pen and financial papers in blue-grey tones"></div>
  <h2>TESTMONIALS</h2>
  <div class="rule"></div>
  <blockquote>Aenean placerat nunc lorem, vitae suscipit mi luctus quis. In ligula lorem, ultricies volutpat arcu et, ultrices cursus enim.</blockquote>
  <svg class="t-arrow" style="left:186px" width="16" height="28"><path d="M13 2 3 14l10 12" stroke="#fff" stroke-width="2.5" fill="none"/></svg>
  <svg class="t-arrow" style="left:1018px" width="16" height="28"><path d="M3 2l10 12L3 26" stroke="#fff" stroke-width="2.5" fill="none"/></svg>
  <div class="avatar" role="img" aria-label="Customer portrait placeholder"></div>
  <div class="name">Daniel Brooks</div>
</section>

<section class="newsletter">
  <svg class="abs" style="left:148px;top:20px" width="38" height="36"><path d="M2 18 36 2 28 34 18 24zM18 24l18-22" fill="none" stroke="#fff" stroke-width="2.5" stroke-linejoin="round"/></svg>
  <div class="label">Subscribe to<br>our Newsletter</div>
  <div class="nl-input" style="left:379px;width:253px">Enter Your Name</div>
  <div class="nl-input" style="left:655px;width:254px">Enter Your Email Address</div>
  <div class="nl-btn">SUBSCRIBE</div>
</section>

<footer class="site-footer">
  <h4 style="left:111px;top:26px">Social Links</h4>
  <div class="f-social"><i class="on"></i><i></i><i></i></div>
  <h4 style="left:111px;top:142px">Blogs</h4>
  <div class="blog">
    <div class="t">Post Title</div>
    <div class="d">Friday, 08 August 2014</div>
    <p>Lorem ipsum dolor sit amet, consectetur adipiscing elit. Nunc non diam erat. In fringilla mauris ut nisi ullamcorper pellentesque.</p>
    <a href="#">Read More »</a>
  </div>

  <h4 style="left:447px;top:26px">Advertise With Us</h4>
  <ul class="ad-list">
    <li>Lorem ipsum dolor sit</li>
    <li>Amet consectetur</li>
    <li>Praesent vel sem id</li>
    <li>Curabitur hendrerit est</li>
    <li>Aliquam eget erat nec sapien</li>
    <li>Cras id augue nunc</li>
    <li>In nec justo non</li>
    <li>Vivamus mollis enim ut</li>
    <li>Curabitur hendrerit est</li>
  </ul>

  <h4 style="left:819px;top:26px">Contact Us</h4>
  <div class="f-field" style="top:66px;height:28px">Name</div>
  <div class="f-field" style="top:102px;height:30px">Email</div>
  <div class="f-field" style="top:142px;height:113px">Massages</div>
  <div class="f-submit">SUBMIT</div>
</footer>

<div class="bottom-bar"><span>Copyright © 2014 - All Rights Reserved</span></div>

</body>
</html>
```